Website design for legal tech start up in Switzerland (B2B)

We are for a legal tech start up in Switzerland called TAVO. We have been running since August 2016. This will be our first live website.

We need a website designed and business card design for our start-up in Switzerland. We also need the Web design to be converted into HTML and CSS files.

Function of website:
• To inform potential customers of our services
• Form a key part of our digital marketing and sales footprint.
• Branding

Please find attached logo.
Updates

Project Deadline Extended Reason: Giving us time to review submissions and provide opportunity for more submissions. Added Thursday, February 16, 2017

Reason: Looking for more idea's not necessarily set on blue and grey colours only.

Target Market(s)

B2B tech powered legal services.

Industry/Entity Type

Legal

Contact Information for Business Card

Lean and slick design.

Coding

Coded - Design and coding required

Number of Pages Required

5+ page

Requirements
Must have
• VERY LEAN AND CLEAN DESIGN!
• We have received many great standard designs, but we are looking for something more out-of-the box: You can get inspiration from these designs: http://www.pindelsite.com/websites/clean/
• Thanks!!
• Easy content management system
• Well structured coding for additional development
• Responsive webpage for all types of devices
• SEO optimized
• Tabs (Home, services, team, careers, blog, contact us)
• Colour scheme complementary to logo
Nice to have
• Look and Design - Approachable, High-tech, Modern
• Easy to add chat bot capability in future
Should not have
• Too busy/ too much clutter
• Not take to long to load

```html
<!DOCTYPE html>
<html lang="en">
<head>
<meta charset="utf-8">
<title>TAVO – Legal Tech Services</title>
<link rel="stylesheet" href="https://fonts.googleapis.com/css2?family=Arimo:wght@400;700&family=Tinos:ital,wght@0,400;0,700;1,400&display=swap">
<style>
:root{
  --navy:#1d4677;
  --navy-dark:#14355c;
  --navy-light:#2a5d96;
  --accent:#2c65a8;
  --grey-text:#444;
  --body-text:#555;
  --rule:#cfcfcf;
  --hex-border:#dcdcdc;
  --white:#fff;
  --footer-bar:#3a3a3a;
}
*{margin:0;padding:0;box-sizing:border-box}
html,body{width:1200px;height:2510px;overflow:hidden;background:var(--white)}
body{position:relative;font-family:"Tinos",serif;color:var(--grey-text)}
.abs{position:absolute}
.brand{font-family:"Arimo",sans-serif;font-weight:700;color:#3d3d3d;letter-spacing:4px}

/* header */
.top-tab{left:728px;top:0;width:472px;height:34px;background:#e6e6e6;border-bottom-left-radius:18px}
.top-tab .phone{position:absolute;left:26px;top:8px;font:13px "Arimo",sans-serif;color:var(--navy);display:flex;gap:8px;align-items:center}
.social{display:flex;gap:6px}
.social span{width:24px;height:24px;border-radius:50%;background:var(--navy);display:block}
.top-tab .social{position:absolute;left:232px;top:5px}
.logo-head{left:160px;top:22px;font-size:64px;line-height:72px}
.cta{left:795px;top:55px;width:235px;height:40px;background:var(--navy);color:#fff;font:14px "Tinos",serif;letter-spacing:.5px;display:flex;align-items:center;justify-content:center;border-radius:2px}

.main-nav{left:0;top:104px;width:1200px;height:43px;background:linear-gradient(#2b5b92,var(--navy-dark))}
.main-nav a{position:absolute;top:13px;color:#fff;font-size:14px;text-decoration:none}
.main-nav .follow{position:absolute;left:787px;top:13px;color:#fff;font-size:14px}
.main-nav .social{position:absolute;left:900px;top:9px}
.main-nav .social span{background:transparent;border:1.5px solid #cfd8e4}

/* hero */
.hero{left:0;top:147px;width:1200px;height:503px;background:radial-gradient(circle at 30% 40%,#d2e2f2 0%,#8fb0d2 35%,#3c5f86 65%,#1c2d44 100%)}
.hero-caption{left:0;top:591px;width:1200px;height:59px;background:rgba(20,25,35,.78);color:#fff;font:26px "Arimo",sans-serif;text-align:center;line-height:59px}
.slide-arrow{top:375px;width:34px;height:28px;background:#333;color:#fff;display:flex;align-items:center;justify-content:center;font:16px "Arimo",sans-serif}

/* welcome */
.section-title{left:0;width:1200px;text-align:center;font-size:32px;color:#222}
.title-rule{height:1px;background:var(--rule)}
.title-rule::after{content:"";position:absolute;left:50%;top:-1px;width:36px;margin-left:-18px;height:3px;background:var(--accent)}
.welcome-text{left:179px;top:757px;width:842px;text-align:center;font-size:11.5px;line-height:20px;color:var(--body-text)}

/* services */
.services{left:0;top:880px}
.hex-label{font:700 14px "Tinos",serif;fill:#fff}

/* why choose */
.why{left:0;top:1398px;width:1200px;height:435px;background:linear-gradient(#2a5b94,#16375f);overflow:hidden}
.why-title{left:0;top:1444px;width:1200px;text-align:center;color:#fff;font-size:26px}
.why-rule{left:505px;top:1484px;width:190px;height:1px;background:rgba(255,255,255,.4)}
.reason{color:#fff}
.reason h3{font-size:15px;font-weight:400;line-height:19px}
.reason p{font-size:12px;line-height:17px;color:#e6edf5}
.reason.right{text-align:right}
.why-logo{left:435px;top:1742px;width:336px;text-align:center;font-size:78px;line-height:80px}

/* testimonials */
.testi-title{top:1900px;font-size:26px}
.testi-title em{font-style:normal;color:var(--accent)}
.quote{left:235px;top:1978px;width:770px;text-align:center;font:italic 14.5px/25px "Arimo",sans-serif;color:#333}
.quote-mark{font:60px "Tinos",serif;color:#bbb;line-height:60px}
.client{left:0;top:2070px;width:1200px;text-align:center}
.client .name{color:var(--accent);font:15px "Arimo",sans-serif}
.client .place{font:13px "Arimo",sans-serif;color:#333;margin-top:3px}
.dots{left:572px;top:2134px;display:flex;gap:8px}
.dots span{width:9px;height:9px;border-radius:50%;background:#aaa}
.dots span:first-child{background:var(--navy)}

/* footer */
.footer{left:0;top:2183px;width:1200px;height:279px;background:linear-gradient(#25578f,#173a63)}
.foot-head{color:#fff;font-size:17px}
.foot-links{list-style:none;color:#e0e8f2;font-size:12.5px;line-height:22px}
.foot-links li::before{content:"› ";color:#9fb6d1}
.col-rule{width:1px;background:rgba(255,255,255,.25)}
.contact-line{display:flex;gap:10px;align-items:flex-start;color:#fff;font-size:12.5px;line-height:18px}
.contact-line .ico{width:18px;height:18px;border-radius:50%;background:#fff;flex:none}
.field{left:564px;width:206px;background:#fff;border-radius:2px;font:11px "Arimo",sans-serif;color:#444;padding:8px 8px}
.submit{left:564px;top:2412px;width:104px;height:33px;background:#000;color:#fff;font-size:14px;display:flex;align-items:center;justify-content:center;gap:10px}
.footer .social span{width:26px;height:26px;background:#fff}
.foot-brand{left:917px;top:2340px;font-size:36px;color:#dfe7f1;font-family:"Arimo",sans-serif;letter-spacing:4px}
.copyright{left:0;top:2462px;width:1200px;height:48px;background:var(--footer-bar);color:#ddd;font-size:12px;text-align:center;line-height:48px}
</style>
</head>
<body>

<header>
  <div class="abs top-tab">
    <div class="phone">
      <svg width="20" height="20" viewBox="0 0 20 20"><circle cx="10" cy="10" r="10" fill="#1d4677"/><path d="M7 5c1 0 2 2 1.8 2.6L7.4 8.6c.6 1.6 2.2 3.2 4 4l1-1.4c.6-.2 2.6.8 2.6 1.8 0 1-1 2-2 2C8 15 5 12 5 7c0-1 1-2 2-2z" fill="#fff"/></svg>
      Call : 555-014-2270
    </div>
    <div class="social"><span></span><span></span><span></span><span></span></div>
  </div>
  <div class="abs brand logo-head">TAVO</div>
  <div class="abs cta">GET A FREE CONSULTATION</div>
  <nav class="abs main-nav">
    <a style="left:184px">Home</a>
    <a style="left:273px">Services</a>
    <a style="left:375px">Team</a>
    <a style="left:457px">Careers</a>
    <a style="left:552px">Blog</a>
    <a style="left:633px">Contact Us</a>
    <span class="follow">Follow Us On</span>
    <div class="social"><span></span><span></span><span></span><span></span></div>
  </nav>
</header>

<section>
  <div class="abs hero" role="img" aria-label="Photo of a hand touching a glowing gavel icon linked to a network of people icons"></div>
  <div class="abs slide-arrow" style="left:0">‹</div>
  <div class="abs slide-arrow" style="left:1166px">›</div>
  <div class="abs hero-caption">Helping Technology Companies Succeed</div>
</section>

<section>
  <h1 class="abs section-title" style="top:680px;font-weight:400">Welcome to TAVO</h1>
  <div class="abs title-rule" style="left:460px;top:734px;width:280px"></div>
  <p class="abs welcome-text">Lorem ipsum dolor sit amet, consectetuer adipiscing elit, sed diam nonummy nibh euismod tincidunt ut laoreet dolore magna aliquam erat volutpat. Ut wisi enim ad minim veniam, quis nostrud exerci tation ullamcorper suscipit lobortis nisl ut aliquip ex ea commodo consequat. Duis autem vel eum iriure dolor in hendrerit in vulputate velit esse molestie consequat, vel illum dolore eu feugiat nulla facilisis at vero eros et accumsan et iusto odio dignissim qui blandit praesent luptatum zzril delenit augue duis dolore te feugait nulla facilisi. Ut wisi enim ad minim veniam, quis nostrud exerci tation ullamcorper suscipit lobortis nisl ut aliquip ex ea commodo consequat. Duis autem et iusto odio dignissim qui blandit praesent luptatum zzril delenit augue duis dolore te feugait nulla facilisi.</p>
</section>

<section class="abs services">
  <svg width="1200" height="480" viewBox="0 0 1200 480">
    <defs>
      <linearGradient id="g-info" x1="0" y1="0" x2="1" y2="1"><stop offset="0" stop-color="#e8ecf0"/><stop offset="1" stop-color="#7f95ad"/></linearGradient>
      <linearGradient id="g-case" x1="0" y1="0" x2="1" y2="1"><stop offset="0" stop-color="#a9c0d8"/><stop offset="1" stop-color="#4b6584"/></linearGradient>
      <linearGradient id="g-app" x1="0" y1="0" x2="1" y2="1"><stop offset="0" stop-color="#3e5574"/><stop offset="1" stop-color="#121d2c"/></linearGradient>
      <linearGradient id="g-env" x1="0" y1="0" x2="1" y2="1"><stop offset="0" stop-color="#9cc46a"/><stop offset="1" stop-color="#2f5a25"/></linearGradient>
      <linearGradient id="g-word" x1="0" y1="0" x2="1" y2="1"><stop offset="0" stop-color="#8a6e55"/><stop offset="1" stop-color="#2a211c"/></linearGradient>
      <linearGradient id="g-proc" x1="0" y1="0" x2="1" y2="1"><stop offset="0" stop-color="#d8d5d0"/><stop offset="1" stop-color="#6d6862"/></linearGradient>
    </defs>
    <g stroke="#dcdcdc" stroke-width="9" stroke-linejoin="round">
      <polygon role="img" aria-label="Photo of hands reviewing charts and reports" fill="url(#g-info)" points="377,29 482,90 482,210 377,271 272,210 272,90"/>
      <polygon fill="#1d4677" points="603,29 708,90 708,210 603,271 498,210 498,90"/>
      <polygon role="img" aria-label="Photo of a businessman on the phone at his desk" fill="url(#g-case)" points="825,29 930,90 930,210 825,271 720,210 720,90"/>
      <polygon role="img" aria-label="Photo of a finger touching digital application icons" fill="url(#g-app)" points="264,226 369,287 369,407 264,468 159,407 159,287"/>
      <polygon role="img" aria-label="Photo of a green forest canopy" fill="url(#g-env)" points="487,226 592,287 592,407 487,468 382,407 382,287"/>
      <polygon role="img" aria-label="Photo of a person signing legal documents" fill="url(#g-word)" points="711,226 816,287 816,407 711,468 606,407 606,287"/>
      <polygon role="img" aria-label="Photo of ball bearings on technical plans" fill="url(#g-proc)" points="936,226 1041,287 1041,407 936,468 831,407 831,287"/>
    </g>
    <text x="603" y="136" text-anchor="middle" font-family="Tinos,serif" font-size="38" fill="#fff">Our</text>
    <text x="603" y="178" text-anchor="middle" font-family="Tinos,serif" font-size="38" fill="#fff">Services</text>
    <rect x="745" y="180" width="80" height="34" fill="rgba(255,255,255,.25)"/>
    <g class="hex-label" text-anchor="middle">
      <text x="377" y="212">Information Management</text>
      <text x="825" y="212">Case Support</text>
      <text x="264" y="409">Application Development</text>
      <text x="487" y="409">Environmental Litigation</text>
      <text x="711" y="409">Legal Word Processing</text>
      <text x="936" y="409">Procurement Support</text>
    </g>
  </svg>
</section>

<section>
  <div class="abs why"></div>
  <h2 class="abs why-title" style="font-weight:400">Why Choose Us</h2>
  <div class="abs why-rule"></div>
  <svg class="abs" style="left:0;top:1398px" width="1200" height="435" viewBox="0 0 1200 435">
    <circle cx="603" cy="440" r="168" fill="#fff" stroke="#2c65a8" stroke-width="7"/>
    <g stroke="#fff" stroke-width="1.5" fill="none">
      <line x1="372" y1="360" x2="415" y2="330"/>
      <line x1="432" y1="259" x2="485" y2="300"/>
      <line x1="536" y1="209" x2="559" y2="278"/>
      <line x1="665" y1="209" x2="645" y2="278"/>
      <line x1="768" y1="259" x2="720" y2="300"/>
      <line x1="820" y1="360" x2="790" y2="330"/>
    </g>
    <g fill="#fff" stroke="#2c65a8" stroke-width="2">
      <circle cx="458" cy="367" r="6"/><circle cx="485" cy="307" r="6"/><circle cx="559" cy="282" r="6"/>
      <circle cx="645" cy="282" r="6"/><circle cx="720" cy="307" r="6"/><circle cx="752" cy="367" r="6"/>
    </g>
    <g fill="#fff">
      <circle cx="372" cy="360" r="37"/><circle cx="432" cy="259" r="37"/><circle cx="536" cy="209" r="37"/>
      <circle cx="665" cy="209" r="37"/><circle cx="768" cy="259" r="37"/><circle cx="820" cy="360" r="37"/>
    </g>
    <g fill="#1d4677">
      <circle cx="372" cy="355" r="10"/><rect x="366" y="367" width="12" height="8" rx="2"/>
      <circle cx="432" cy="259" r="12"/><circle cx="432" cy="259" r="5" fill="#fff"/>
      <path d="M525 198c3 0 6 5 5 7l-3 3c2 4 5 7 9 9l3-3c2-1 7 2 7 5s-3 5-5 5c-11 0-20-9-20-20 0-3 2-6 4-6z"/>
      <circle cx="660" cy="200" r="9"/><path d="M646 228c0-11 8-16 14-16s14 5 14 16z"/>
      <rect x="754" y="246" width="26" height="24" rx="3"/><rect x="758" y="254" width="18" height="12" fill="#fff"/>
      <circle cx="812" cy="352" r="7"/><circle cx="828" cy="352" r="7"/><path d="M800 374c0-8 5-12 12-12s12 4 12 12zM818 374c0-8 5-12 10-12s12 4 12 12z"/>
    </g>
  </svg>
  <div class="abs reason right" style="left:180px;top:1520px;width:300px"><h3>Unbiased Recommendations</h3><p>Lorem ipsum dolor sit mork<br>[+]...adipiscing sed diam</p></div>
  <div class="abs reason right" style="left:175px;top:1602px;width:200px"><h3>Unparalleled<br>Service</h3><p>Lorem ipsum dolor sit mork<br>[+]...adipiscing sed diam</p></div>
  <div class="abs reason right" style="left:121px;top:1731px;width:200px"><h3>Superior Advice</h3><p>Lorem ipsum dolor sit mork<br>[+]...adipiscing sed diam</p></div>
  <div class="abs reason" style="left:720px;top:1520px;width:220px"><h3>Expert Guidance</h3><p>Lorem ipsum dolor sit mork<br>adipiscing sed diam...[+]</p></div>
  <div class="abs reason" style="left:825px;top:1616px;width:220px"><h3>Considerable Time<br>For You</h3><p>Lorem ipsum dolor sit mork<br>adipiscing sed diam...[+]</p></div>
  <div class="abs reason" style="left:879px;top:1716px;width:220px"><h3>Deep Legal Industry<br>Relationships</h3><p>Lorem ipsum dolor sit mork<br>adipiscing sed diam...[+]</p></div>
  <div class="abs brand why-logo">TAVO</div>
</section>

<section>
  <h2 class="abs section-title testi-title" style="font-weight:400">Clients <em>Testimonials</em></h2>
  <div class="abs title-rule" style="left:478px;top:1946px;width:244px"></div>
  <svg class="abs" style="left:135px;top:1995px" width="26" height="54" viewBox="0 0 26 54"><polyline points="24,2 2,27 24,52" fill="none" stroke="#bbb" stroke-width="2"/></svg>
  <svg class="abs" style="left:1039px;top:1995px" width="26" height="54" viewBox="0 0 26 54"><polyline points="2,2 24,27 2,52" fill="none" stroke="#bbb" stroke-width="2"/></svg>
  <div class="abs quote-mark" style="left:193px;top:1962px">“</div>
  <p class="abs quote">Lorem ipsum dolor sit amet, consectetuer adipiscing elit, sed diam nonummy nibh euismod tinciduntol ut laoreet dolore magna aliquam erat volutpat. Ut wisi enim ad minim veniam, quis nostrud exercimori mornkle tation ullamcorper suscipit lobortis nisl ut aliquip ex ea commodo consequat.</p>
  <div class="abs quote-mark" style="left:768px;top:2028px">”</div>
  <div class="abs client"><div class="name">Mara K.</div><div class="place">Lakeview, CA</div></div>
  <div class="abs dots"><span></span><span></span><span></span><span></span></div>
</section>

<footer>
  <div class="abs footer"></div>
  <h4 class="abs foot-head" style="left:164px;top:2228px;font-weight:400">Quick Links</h4>
  <ul class="abs foot-links" style="left:164px;top:2265px">
    <li>Home</li><li>Services</li><li>Team</li><li>Careers</li><li>Blog</li><li>Contact Us</li>
  </ul>
  <div class="abs col-rule" style="left:292px;top:2228px;height:200px"></div>
  <h4 class="abs foot-head" style="left:316px;top:2228px;font-weight:400">Contact Details</h4>
  <div class="abs" style="left:314px;top:2268px;display:flex;flex-direction:column;gap:14px">
    <div class="contact-line"><span class="ico"></span><span>Tavo Technology<br>Street Name City Name<br>State Zipcode</span></div>
    <div class="contact-line"><span class="ico"></span><span>555-014-2270</span></div>
    <div class="contact-line"><span class="ico"></span><span>555-014-2270</span></div>
    <div class="contact-line"><span class="ico"></span><span>inquiry@tavotechnology.com</span></div>
  </div>
  <div class="abs col-rule" style="left:540px;top:2228px;height:200px"></div>
  <h4 class="abs foot-head" style="left:564px;top:2228px;font-weight:400">Quick Inquiry</h4>
  <div class="abs field" style="top:2270px;height:32px">Name</div>
  <div class="abs field" style="top:2308px;height:32px">Email</div>
  <div class="abs field" style="top:2346px;height:60px">Message</div>
  <div class="abs submit">Submit <span>→</span></div>
  <h4 class="abs foot-head" style="left:932px;top:2234px;font-weight:400">Follow Us</h4>
  <div class="abs social" style="left:922px;top:2270px"><span></span><span></span><span></span><span></span></div>
  <div class="abs foot-brand">TAVO</div>
  <div class="abs copyright">Copyright © 2017 Tavo Technology. All Rights Reserved.</div>
</footer>

</body>
</html>
```